Packiging of mouse trap

We need a packiging for a new mousetrap called 'Quillnest'. It is a mouse/rat trap. We want to have it pretty simple and modern. The logo of the mouse trap is in the attachment and the measures of the packaging also (don't look at the design, it has nothing to do with us). It's needs to stand out in between the other packaging due to it's simplicity and modern touch.

Font styles to use
Sans Serif

Requirements
Must have
• Simplicity, modern
Should not have
• Too many colors

```html
<!DOCTYPE html>
<html lang="en">
<head>
<meta charset="utf-8">
<title>Quillnest Electronic Mouse Trap Packaging</title>
<link rel="stylesheet" href="https://fonts.googleapis.com/css2?family=Archivo+Black&family=Barlow+Condensed:wght@500&family=Arimo:wght@400;700&display=swap">
<style>
  :root {
    --ink: #1f2424;
    --lime: #cfdf4a;
    --product-dark: #1a1a1a;
    --product-mid: #3a3b3c;
    --page: #ffffff;
  }
  * { margin: 0; padding: 0; box-sizing: border-box; }
  html, body { width: 1200px; height: 1200px; overflow: hidden; background: var(--page); }
  .sheet {
    position: relative; width: 1200px; height: 1200px;
    display: flex; gap: 30px; padding: 140px 60px;
  }
  .panel {
    position: relative; width: 340px; height: 920px; overflow: hidden;
    box-shadow: 0 10px 30px rgba(0,0,0,0.18);
  }
  .panel--front { background: var(--ink); }
  .panel--side { background: var(--lime); }
  .panel--back { background: var(--ink); border-left: 3px solid var(--lime); }
  .panel-wedge { position: absolute; inset: 0; width: 100%; height: 100%; }
  .brand-name {
    position: absolute; left: 24px; top: 120px;
    font-family: "Archivo Black", sans-serif; font-size: 48px; line-height: 1;
    letter-spacing: -1px; white-space: nowrap;
  }
  .panel--front .brand-name { color: var(--lime); }
  .panel--side .brand-name { color: var(--ink); }
  .product-type {
    position: absolute; left: 60px; top: 250px;
    font-family: "Barlow Condensed", sans-serif; font-weight: 500;
    font-size: 30px; line-height: 1.08; text-transform: uppercase;
  }
  .panel--front .product-type { color: var(--lime); }
  .panel--side .product-type { color: var(--ink); }
  .product-shot {
    position: absolute; left: 80px; top: 480px; width: 200px; height: 370px;
    border-radius: 26px;
    background: linear-gradient(135deg, var(--product-mid), var(--product-dark) 70%);
  }
  .panel--side .product-shot { left: 90px; top: 430px; }
  .back-copy {
    position: relative; padding: 50px 22px 0 30px;
    font-family: Arimo, sans-serif; color: var(--lime);
  }
  .back-headline { font-weight: 700; font-size: 12.5px; text-transform: uppercase; letter-spacing: .3px; margin-bottom: 14px; white-space: nowrap; }
  .feature { margin-bottom: 10px; }
  .feature-title { font-weight: 700; font-size: 12px; text-transform: uppercase; }
  .feature-text { font-size: 11.5px; }
  .battery-note {
    display: inline-block; background: var(--lime); color: var(--ink);
    font-size: 10px; padding: 2px 5px; margin: 4px 0 24px; white-space: nowrap;
  }
  .warning-title { font-weight: 700; font-size: 15px; letter-spacing: 1px; margin-bottom: 6px; }
  .warning-text { font-size: 11.5px; line-height: 1.6; margin-bottom: 26px; }
  .tag { background: var(--lime); color: var(--ink); padding: 0 4px; white-space: nowrap; }
  .legal {
    position: absolute; left: 140px; bottom: 40px;
    font-family: Arimo, sans-serif; color: var(--lime); font-size: 11.5px; line-height: 1.35;
  }
</style>
</head>
<body>
<main class="sheet">
  <section class="panel panel--front">
    <svg class="panel-wedge" viewBox="0 0 340 920" preserveAspectRatio="none" aria-hidden="true">
      <polygon points="340,110 340,920 30,920" fill="var(--lime)"/>
    </svg>
    <h1 class="brand-name">Quillnest</h1>
    <p class="product-type">Electronic<br>Mouse<br>Trap</p>
    <div class="product-shot" role="img" aria-label="Photo of the black electronic trap with a mouse entering its tunnel"></div>
  </section>

  <section class="panel panel--side">
    <svg class="panel-wedge" viewBox="0 0 340 920" preserveAspectRatio="none" aria-hidden="true">
      <polygon points="0,0 60,0 0,160" fill="var(--ink)"/>
      <polygon points="340,70 340,920 130,920" fill="var(--ink)"/>
    </svg>
    <h2 class="brand-name">Quillnest</h2>
    <p class="product-type">Electronic<br>Mouse<br>Trap</p>
    <div class="product-shot" role="img" aria-label="Photo of the trap seen from above with its switch and a mouse at the side"></div>
  </section>

  <section class="panel panel--back">
    <svg class="panel-wedge" viewBox="0 0 340 920" preserveAspectRatio="none" aria-hidden="true">
      <polygon points="0,0 30,0 0,180" fill="var(--lime)"/>
    </svg>
    <div class="back-copy">
      <p class="back-headline">4 AA batteries eliminate up to 90 mice</p>
      <div class="feature"><p class="feature-title">Quick &amp; Humane</p><p class="feature-text">Humanely removes up to 90 rodents</p></div>
      <div class="feature"><p class="feature-title">Smart Rodent Detection</p><p class="feature-text">Built-in safety sensors to protect kids and pets</p></div>
      <div class="feature"><p class="feature-title">Easy Cleanups</p><p class="feature-text">No-touch, no-see, no-mess disposal</p></div>
      <div class="feature"><p class="feature-title">New &amp; Improved Design</p><p class="feature-text">Efficient zap system with no-escape tunnel design</p></div>
      <p class="battery-note">Each Mouse Trap Requires 4 AA Batteries (Not Included)</p>
      <p class="warning-title">WARNING</p>
      <p class="warning-text"><span class="tag">Electric Shock and Spark Hazards</span><br><span class="tag">Ignition:</span> Use indoors on dry, clean surfaces. Do not use near flammable vapors, liquids or solids. <span class="tag">High Voltage:</span> Keep out of reach of children and pets. Turn off the power before placing the bait. <span class="tag">Electromagnetic Waves:</span> Keep pacemakers at least one foot away. Please read and follow all label instructions.</p>
      <p class="warning-title">WARNING</p>
      <p class="warning-text">This product may expose you to lead or other chemicals known to cause cancer or birth defects. For more information go to www.labelsafetyinfo.org.</p>
    </div>
    <p class="legal">Electronic Mouse Trap<br>US. Pat 00000000<br>EPA Est.No:00000-XX<br>www.quillnesthome.com<br>Design in USA<br>Made in China</p>
  </section>
</main>
</body>
</html>
```